Fahnendesign für Lenz & Baumer Elektrotechnik
Zielgruppe
Lenz & Baumer Elektrotechnik hat sich spezialisiert auf die Errichtung elektrischer Anlagen im Wohn-Neubau und bei Sanierungen von Wohnungen und Einfamilienhäusern. Unsere Zielgruppe sind Bauunternehmen und private Bauherren.
Aufgabenstellung
-Design nach Vorgaben Druckfalke ( Befestigung links )
Natürlich soll unser Logo gut zu sehen sein sowie unsere Internetseite : www.lenz-baumer.de
Firmenschriftart: Titel Fira Sans , Schrift : Montserrat
Vielleicht kann ein Bezug auf die Positionierung hergestellt werden , ist aber kein muss.
Alles andere kann kreativ entschieden werden. Schaut gerne auf unsere Social Media Kanäle:
https://www.instagram.com/lenz_baumer_elektrotechnik/?hl=de
https://www.facebook.com/lenzbaumerelektrotechnik/

```html
<!DOCTYPE html>
<html lang="de">
<head>
<meta charset="utf-8">
<title>Lenz &amp; Baumer Elektrotechnik – Fahnen</title>
<link href="https://fonts.googleapis.com/css2?family=Fira+Sans:wght@600&family=Montserrat:wght@400;500&display=swap" rel="stylesheet">
<style>
  :root {
    --brand-blue: #0a84c6;
    --white: #ffffff;
    --canvas: #ffffff;
    --faint: rgba(255,255,255,0.08);
  }
  * { margin: 0; padding: 0; box-sizing: border-box; }
  html, body { width: 1082px; height: 1200px; overflow: hidden; background: var(--canvas); }
  .stage { position: relative; width: 1082px; height: 1200px; }

  .flag {
    position: absolute; top: 163px; width: 326px; height: 869px;
    background: var(--white); overflow: hidden;
    box-shadow: 0 6px 22px rgba(0,0,0,0.12);
  }
  .flag--front { left: 143px; }
  .flag--back { left: 609px; }

  .brand {
    position: absolute; text-align: center; color: var(--brand-blue);
    font-family: "Fira Sans", sans-serif; font-weight: 600; line-height: 1.1;
  }
  .brand__mark {
    display: block; margin: 0 auto 14px; width: 70px; height: 70px;
    border: 4px solid var(--brand-blue); border-radius: 50%;
  }
  .brand__name { display: block; font-size: 28px; letter-spacing: 0.5px; }
  .brand__tag { display: block; font-size: 12px; letter-spacing: 3px; margin-top: 6px; }

  .flag--front .brand { left: 0; width: 326px; top: 68px; }

  .flag__shape { position: absolute; inset: 0; }

  .contact-list {
    position: absolute; left: 30px; top: 672px; list-style: none;
    font-family: "Montserrat", sans-serif; font-size: 18px; color: var(--white);
    letter-spacing: -0.4px;
  }
  .contact-list li { display: flex; align-items: center; height: 30px; margin-bottom: 28px; }
  .contact-list .icon { width: 28px; height: 28px; margin-right: 11px; flex: none; }

  .flag--back .side-band {
    position: absolute; right: 0; top: 0; width: 76px; height: 869px; background: var(--brand-blue);
  }
  .side-band__rule { position: absolute; left: 37px; width: 2px; background: var(--white); }
  .side-band__rule--top { top: 100px; height: 118px; }
  .side-band__rule--bottom { top: 669px; height: 117px; }
  .side-band__url {
    position: absolute; left: 38px; top: 434px; white-space: nowrap;
    transform: translate(-50%, -50%) rotate(-90deg);
    font-family: "Montserrat", sans-serif; font-size: 22px; color: var(--white); letter-spacing: 4.5px;
  }
  .flag--back .brand {
    left: 131px; top: 434px; width: 330px;
    transform: translate(-50%, -50%) rotate(-90deg);
  }
</style>
</head>
<body>
<main class="stage">

  <section class="flag flag--front" aria-label="Fahne Vorderseite">
    <svg class="flag__shape" width="326" height="869" viewBox="0 0 326 869" aria-hidden="true">
      <polygon points="0,358 326,274 326,288 0,372" fill="var(--brand-blue)"/>
      <polygon points="0,382 326,298 326,869 0,869" fill="var(--brand-blue)"/>
      <circle cx="163" cy="500" r="140" fill="none" stroke="var(--faint)" stroke-width="8"/>
    </svg>

    <div class="brand">
      <span class="brand__mark"></span>
      <span class="brand__name">LENZ &amp; BAUMER</span>
      <span class="brand__tag">ELEKTROTECHNIK</span>
    </div>

    <ul class="contact-list">
      <li>
        <svg class="icon" viewBox="0 0 28 28" aria-hidden="true">
          <g fill="none" stroke="#fff" stroke-width="1.8">
            <circle cx="14" cy="14" r="11"/>
            <ellipse cx="14" cy="14" rx="5" ry="11"/>
            <line x1="3" y1="14" x2="25" y2="14"/>
            <line x1="5" y1="8.5" x2="23" y2="8.5"/>
            <line x1="5" y1="19.5" x2="23" y2="19.5"/>
          </g>
        </svg>
        www.lenz-baumer.de
      </li>
      <li>
        <svg class="icon" viewBox="0 0 28 28" aria-hidden="true"><circle cx="14" cy="14" r="12" fill="#fff"/></svg>
        lenz_baumer_elektrotechnik
      </li>
      <li>
        <svg class="icon" viewBox="0 0 28 28" aria-hidden="true"><circle cx="14" cy="14" r="12" fill="#fff"/></svg>
        @lenzbaumerelektrotechnik
      </li>
    </ul>
  </section>

  <section class="flag flag--back" aria-label="Fahne Rückseite">
    <div class="brand">
      <span class="brand__mark"></span>
      <span class="brand__name">LENZ &amp; BAUMER</span>
      <span class="brand__tag">ELEKTROTECHNIK</span>
    </div>
    <div class="side-band">
      <span class="side-band__rule side-band__rule--top"></span>
      <span class="side-band__url">www.lenz-baumer.de</span>
      <span class="side-band__rule side-band__rule--bottom"></span>
    </div>
  </section>

</main>
</body>
</html>
```